Design a company business card

Design a business card based on our logo. Would like colors of the Philippine flag as the base design of the card. Using the attached color and Pantone. All entries who doesn’t comply to the color and design requirement will not be considered. I have attached our company logo. Company logo must be incorporated. A bit of information about our company, we are a Home Care Agency.

```html
<!DOCTYPE html>
<html lang="en">
<head>
<meta charset="utf-8">
<title>Luma Home Care Agency – Business Card</title>
<link rel="stylesheet" href="https://fonts.googleapis.com/css2?family=Montserrat:wght@700;800&family=Lato:wght@400;700&display=swap">
<style>
  :root {
    --flag-blue: #0038a8;
    --flag-red: #ce1126;
    --flag-yellow: #fcd116;
    --white: #ffffff;
    --backdrop: #3a3440;
    --card-w: 530px;
    --card-h: 303px;
  }
  * { margin: 0; padding: 0; box-sizing: border-box; }
  html, body { width: 1200px; height: 800px; overflow: hidden; }
  body {
    background: var(--backdrop);
    font-family: "Lato", sans-serif;
    position: relative;
  }
  .card {
    position: absolute;
    top: 248px;
    width: var(--card-w);
    height: var(--card-h);
    overflow: hidden;
    box-shadow: 0 10px 30px rgba(0,0,0,0.35);
  }
  .card-back { left: 50px; background: var(--flag-blue); }
  .card-front { left: 620px; }
  .card-art { position: absolute; inset: 0; }

  .wordmark {
    position: absolute;
    font-family: "Montserrat", sans-serif;
    font-weight: 800;
    line-height: 1;
    display: flex;
    flex-direction: column;
    align-items: flex-start;
  }
  .wordmark-row { display: flex; align-items: center; gap: 10px; }
  .wordmark-dot { border-radius: 50%; background: var(--flag-red); }
  .wordmark-name { letter-spacing: 2px; }
  .wordmark-tag { letter-spacing: 1px; margin-top: 6px; }

  .card-back .wordmark {
    left: 50%; top: 50%;
    transform: translate(-50%, -50%);
    color: var(--white);
  }
  .card-back .wordmark-dot { width: 26px; height: 26px; }
  .card-back .wordmark-name { font-size: 46px; }
  .card-back .wordmark-tag { font-size: 14px; }

  .card-front .wordmark { left: 22px; top: 112px; color: var(--flag-blue); }
  .card-front .wordmark-dot { width: 18px; height: 18px; }
  .card-front .wordmark-name { font-size: 32px; }
  .card-front .wordmark-tag { font-size: 10px; margin-top: 4px; }

  .contact {
    position: absolute;
    right: 16px;
    top: 170px;
    text-align: right;
    color: var(--white);
  }
  .contact-name {
    font-family: "Montserrat", sans-serif;
    font-weight: 800;
    font-size: 16px;
    color: var(--flag-yellow);
    letter-spacing: 1px;
  }
  .contact-role {
    display: inline-block;
    font-size: 12px;
    margin-top: 2px;
    padding-bottom: 2px;
    border-bottom: 2px solid var(--flag-yellow);
  }
  .contact-list { list-style: none; margin-top: 8px; }
  .contact-item {
    display: flex;
    justify-content: flex-end;
    align-items: center;
    gap: 6px;
    font-size: 11px;
    line-height: 18px;
  }
  .contact-icon { width: 12px; height: 12px; flex: none; }
</style>
</head>
<body>

<section class="card card-back">
  <div class="wordmark">
    <div class="wordmark-row">
      <span class="wordmark-name">LUMA</span>
      <span class="wordmark-dot"></span>
    </div>
    <span class="wordmark-tag">HOME CARE AGENCY</span>
  </div>
</section>

<section class="card card-front">
  <svg class="card-art" viewBox="0 0 530 303" width="530" height="303">
    <rect x="0" y="0" width="530" height="303" fill="var(--flag-blue)"/>
    <rect x="0" y="150" width="530" height="120" fill="var(--flag-red)"/>
    <polygon points="0,0 262,151 0,303" fill="var(--white)"/>
  </svg>

  <div class="wordmark">
    <div class="wordmark-row">
      <span class="wordmark-name">LUMA</span>
      <span class="wordmark-dot"></span>
    </div>
    <span class="wordmark-tag">HOME CARE AGENCY</span>
  </div>

  <div class="contact">
    <p class="contact-name">MARCO REYES</p>
    <p class="contact-role">Founder</p>
    <ul class="contact-list">
      <li class="contact-item">555 014 2276
        <svg class="contact-icon" viewBox="0 0 12 12"><circle cx="6" cy="6" r="6" fill="var(--flag-yellow)"/><path d="M4 3 L5 3 L5.5 4.5 L4.8 5 Q5.5 6.8 7 7.2 L7.5 6.5 L9 7 L9 8 Q6 9 3.5 4 Z" fill="var(--flag-blue)"/></svg>
      </li>
      <li class="contact-item">hello@lumacare.com
        <svg class="contact-icon" viewBox="0 0 12 12"><circle cx="6" cy="6" r="6" fill="var(--flag-yellow)"/><rect x="3" y="4" width="6" height="4" fill="none" stroke="var(--flag-blue)" stroke-width="0.9"/><path d="M3 4 L6 6.3 L9 4" fill="none" stroke="var(--flag-blue)" stroke-width="0.9"/></svg>
      </li>
      <li class="contact-item">www.lumacare.com
        <svg class="contact-icon" viewBox="0 0 12 12"><circle cx="6" cy="6" r="6" fill="var(--flag-yellow)"/><circle cx="6" cy="6" r="3" fill="none" stroke="var(--flag-blue)" stroke-width="0.9"/><path d="M3 6 H9 M6 3 V9" stroke="var(--flag-blue)" stroke-width="0.7"/></svg>
      </li>
      <li class="contact-item">72 Harbor Lane Millbrook, ON L0A 1G0
        <svg class="contact-icon" viewBox="0 0 12 12"><circle cx="6" cy="6" r="6" fill="var(--flag-yellow)"/><path d="M6 9.5 L3.8 5.8 A2.4 2.4 0 1 1 8.2 5.8 Z" fill="var(--flag-blue)"/><circle cx="6" cy="4.8" r="0.9" fill="var(--flag-yellow)"/></svg>
      </li>
    </ul>
  </div>
</section>

</body>
</html>
```